Sales Page Header Design Project

Hi,
I need a background image created for this sales page: http://tidyventurecamp.example
Width: 977 px
Height: 150 px
Here are a few sample designs to work with: http://marketsummitschool.example/
http://crafthousepixel.example/wp-content/uploads/2011/02/experts1.png
Must be sharp, professional looking and uncluttered.
Colours: Must include blue (I like the blue on the on the current sales page, but will leave shade and colour combinations to your creativity)
Text = Tunde Marwick Presents
Tidy Venture Camp
Your Blueprint for Building a Profitable, Sustainable Business in Today's Economy!
Any questions, give me a shout
Entrepreneurs and Business Owners, aged 21 to 45
Business

```html
<!DOCTYPE html>
<html lang="en">
<head>
<meta charset="utf-8">
<title>Tidy Venture Camp — Sales Page Header</title>
<link rel="stylesheet" href="https://fonts.googleapis.com/css2?family=Cinzel:wght@700;800&family=Crimson+Text:wght@600&display=swap">
<style>
  :root {
    --page-bg: #ececec;
    --banner-center: #2f86c6;
    --banner-mid: #1c5f92;
    --banner-edge: #0a2438;
    --title-white: #ffffff;
    --presenter-ink: #0b0f14;
    --tagline-lime: #d8f21a;
    --icon-dark: #0b0f14;
    --icon-blue: #3aa6e0;
  }
  * { margin: 0; padding: 0; box-sizing: border-box; }
  html, body {
    width: 1200px;
    height: 1000px;
    overflow: hidden;
    background: var(--page-bg);
  }
  .canvas {
    position: relative;
    width: 1200px;
    height: 1000px;
  }
  .header-banner {
    position: absolute;
    left: 112px;
    top: 425px;
    width: 977px;
    height: 150px;
    background:
      radial-gradient(ellipse 55% 140% at 50% 55%, var(--banner-center) 0%, var(--banner-mid) 55%, var(--banner-edge) 100%);
    text-align: center;
    color: var(--title-white);
  }
  .presenter {
    position: absolute;
    top: 12px;
    left: 0;
    right: 0;
    font-family: "Crimson Text", Georgia, serif;
    font-weight: 600;
    font-size: 20px;
    letter-spacing: 0.5px;
    color: var(--presenter-ink);
  }
  .presenter .presents {
    font-size: 11px;
    letter-spacing: 1.5px;
    margin-left: 3px;
  }
  .title {
    position: absolute;
    top: 50px;
    left: 0;
    right: 0;
    display: flex;
    justify-content: center;
    align-items: flex-end;
    gap: 18px;
    font-family: "Cinzel", "Times New Roman", serif;
    font-weight: 800;
    font-size: 54px;
    line-height: 54px;
    letter-spacing: 2px;
    font-variant: small-caps;
    color: var(--title-white);
    text-shadow: 2px 3px 3px rgba(0, 0, 0, 0.75);
  }
  .title-mark {
    width: 62px;
    height: 56px;
    margin-bottom: -2px;
    border-radius: 3px;
    background: linear-gradient(90deg, var(--icon-dark) 0%, var(--icon-dark) 40%, var(--icon-blue) 60%, var(--icon-blue) 100%);
    opacity: 0.9;
  }
  .tagline {
    position: absolute;
    top: 118px;
    left: 0;
    right: 0;
    font-family: "Cinzel", "Times New Roman", serif;
    font-weight: 700;
    font-size: 13px;
    letter-spacing: 1.3px;
    font-variant: small-caps;
    font-style: oblique;
    color: var(--tagline-lime);
    text-shadow: 1px 1px 1px rgba(0, 0, 0, 0.6);
  }
</style>
</head>
<body>
  <div class="canvas">
    <header class="header-banner">
      <p class="presenter">Tunde Marwick <span class="presents">Presents</span></p>
      <h1 class="title">
        <span>Tidy Venture</span>
        <span class="title-mark" role="img" aria-label="Small illustration of a businessman beside rising bars and an upward arrow"></span>
        <span>Camp</span>
      </h1>
      <p class="tagline">Your Blueprint for Building a Profitable, Sustainable Business in Today's Economy!</p>
    </header>
  </div>
</body>
</html>
```